Website Design for a "Talent Recruitment Agency"

We are looking for a website design for the website of our "Talent Recruitment Agency"; which is called "Crestway Hub".
Our recruitment website "Crestway Hub" will be focusing on: "Crestway Hub: Linking People & Firms in Switzerland"; which means our target audience is two-folded:
(i) TALENT - that is currently residing in- or outside of Switzerland, and is open for and interested in the "Swiss Job Market".
(ii) COMPANIES - that are looking for talent for specific job vacancies in Switzerland.
With our "Crestway Hub" approach we inted to focus on Membership & Partnership:
(a)"Membership"(TALENT)
and
(b)"Partnership"(COMPANIES)
Some of the competitor sites we like are:
• www.plimora42.dk
• www.qelvo.ch
• www.brandolix.ch/en
A sitemap example of our website is attached.
Also attached is a "Crestway Hub" logo in .eps format and one in .jpeg format.
We very much look forward to receive your creative ideas.
Best regards,
Crestway Hub
Crestway Hub: Linking People & Firms in Switzerland.
Website: crestwayhub.ch - Chirpline: CrestwayHubCH
Target Market(s)
(i) TALENT (with around 0-10 years of working experience), currently residing in- or outside of Switzerland, but eligible to work in Switzerland.
(ii) COMPANIES (national or international) that are based in Switzerland.
Industry/Entity Type
Recruitment

```html
<!DOCTYPE html>
<html lang="en">
<head>
<meta charset="utf-8">
<title>Crestway Hub – Home</title>
<link href="https://fonts.googleapis.com/css2?family=Lato:ital,wght@0,300;0,400;0,700;0,900;1,400&family=Roboto+Condensed:wght@400;700&display=swap" rel="stylesheet">
<style>
:root{
  --orange:#f25a0f;
  --orange-dark:#c94607;
  --blue:#1478c8;
  --blue-light:#2b9ad8;
  --text:#555;
  --text-dark:#333;
  --muted:#888;
  --topbar:#dbe6f0;
  --page:#f2f2f2;
  --footer:#e9e9e9;
  --bottom:#333;
}
*{margin:0;padding:0;box-sizing:border-box}
html,body{width:1024px;height:1200px;overflow:hidden}
body{font-family:"Lato",sans-serif;color:var(--text);background:var(--page);position:relative}
.abs{position:absolute}

/* top bar */
.topbar{left:0;top:0;width:1024px;height:24px;background:var(--topbar)}
.lang{left:669px;top:0;height:24px;width:122px;display:flex;gap:8px;align-items:center;padding-left:5px}
.lang .current{background:#fff;position:absolute;left:0;top:0;width:28px;height:24px}
.flag{position:relative;width:20px;height:12px;display:flex}
.flag span{flex:1}
.account{right:132px;top:6px;font-size:9px;color:#666;display:flex;gap:25px}

/* header */
.header{left:0;top:24px;width:1024px;height:80px;background:#fff;border-bottom:1px solid #e4e4e4}
.brand{display:flex;align-items:center;gap:10px}
.brand .dot{width:40px;height:40px;border-radius:50%;background:var(--orange)}
.brand .name{font-family:"Lato",sans-serif;font-weight:700;color:var(--orange);font-size:32px;letter-spacing:.2px}
.header .brand{left:133px;top:20px}
.nav{right:136px;top:33px;display:flex;font-size:12px;color:#555}
.nav a{color:inherit;text-decoration:none;padding:0 10px;border-left:1px solid #ccc;line-height:12px}
.nav a:first-child{border-left:0}
.nav a.active{color:var(--orange);font-weight:700}
.nav-underline{left:502px;top:102px;width:36px;height:2px;background:var(--orange)}

/* hero */
.hero-bg{left:0;top:104px;width:1024px;height:401px;background:#f3f3f3}
.map-fill{top:180px;width:129px;height:300px;background:radial-gradient(ellipse at center,#c9def0 0%,rgba(201,222,240,0) 70%)}
.hero-photo{left:129px;top:104px;width:768px;height:401px;background:linear-gradient(100deg,#b9cfe0 0%,#d9e7f2 45%,#e9f1f8 70%,#d6e4ee 100%)}
.hero-person{left:129px;top:115px;width:360px;height:390px;background:linear-gradient(180deg,#caa891 0%,#b78f77 30%,#4a5561 55%,#3b4450 100%);border-radius:140px 140px 0 0;opacity:.85}
.hero-title{left:522px;top:228px;font-weight:900;color:var(--blue);font-size:38px;line-height:37px;letter-spacing:-.3px}
.hero-sub{left:525px;top:314px;font-weight:300;color:#6a7f92;font-size:19px;line-height:23px}
.arrow{top:266px;width:48px;height:48px;background:rgba(130,130,130,.75);display:flex;align-items:center;justify-content:center}
.dots{left:818px;top:481px;display:flex;gap:8px;align-items:center}
.dots i{width:8px;height:8px;border-radius:50%;background:#7f9ab3;display:block}
.dots i.on{width:10px;height:10px;background:var(--blue);border:2px solid #fff}

/* promo band */
.band{left:0;top:505px;width:1024px;height:285px;background:linear-gradient(180deg,#1e5fa4 0%,#2e7fc4 60%,#4aa3dc 100%);overflow:hidden}
.band-shade{left:645px;top:505px;width:379px;height:285px;background:rgba(20,60,120,.18);clip-path:polygon(16px 0,100% 0,100% 100%,0 100%)}
.card{top:544px;width:368px;height:210px;background:#f4f6f8;border-bottom:3px solid #c9d6e2;overflow:hidden}
.card .photo{position:absolute;top:0;height:207px}
.card p{position:absolute;font-weight:300;color:#333;font-size:19px;line-height:28px}
.btn{position:absolute;background:var(--orange);color:#fff;font-weight:700;font-size:14px;width:136px;height:41px;border-radius:3px;border-bottom:3px solid var(--orange-dark);display:flex;align-items:center;justify-content:center}

/* content */
.section-title{font-weight:700;font-size:14px;color:var(--text-dark);letter-spacing:.6px;display:flex;align-items:center;gap:20px}
.section-title .rule{height:6px;background:repeating-linear-gradient(135deg,#d4d4d4 0 1px,transparent 1px 3px)}
.job-card{left:138px;top:850px;width:497px;height:115px;background:#fff;border:1px solid #e6e6e6}
.job-thumb{position:absolute;left:19px;top:17px;width:78px;height:80px;background:#fff;border:1px solid #e3e3e3;padding:3px}
.job-thumb .img{width:100%;height:100%;background:linear-gradient(180deg,#9bb3c9 0%,#6d8298 60%,#3e4b5a 100%)}
.job-thumb .tool{position:absolute;bottom:-4px;width:17px;height:17px;background:var(--blue-light);border-radius:2px;display:flex;align-items:center;justify-content:center}
.job-title{position:absolute;left:112px;top:22px;font-family:"Roboto Condensed",sans-serif;font-weight:700;font-size:14px;color:var(--text-dark)}
.job-loc{position:absolute;left:112px;top:39px;font-family:"Roboto Condensed",sans-serif;font-size:11px;color:#888}
.job-text{position:absolute;left:111px;top:67px;width:370px;font-size:10.5px;line-height:15.5px;color:#666}
.job-text a{color:var(--blue-light);text-decoration:none}
.job-dots{position:absolute;left:357px;top:28px;display:flex;gap:5px}
.job-dots i{width:8px;height:8px;border-radius:50%;background:#e4e4e4;display:block}
.job-dots i.on{background:var(--blue-light)}
.event{left:646px;width:244px;display:flex;gap:12px}
.event .thumb{width:43px;height:43px;flex:none;background:linear-gradient(160deg,#9fb0c0,#4d5b68)}
.event p{font-size:10px;line-height:16px;color:#3b5b8a}
.event time{display:block;font-size:8px;font-style:italic;color:#888;margin-top:1px}

/* footer */
.footer{left:0;top:992px;width:1024px;height:170px;background:var(--footer);border-top:1px solid #dcdcdc}
.footer .brand{left:136px;top:1016px}
.footer .brand .dot{width:32px;height:32px}
.footer .brand .name{font-size:24px}
.footer-about{left:136px;top:1066px;width:220px;font-size:11px;line-height:16px;color:#555}
.fcol h4{font-family:"Roboto Condensed",sans-serif;font-weight:400;font-size:13px;color:#333;margin-bottom:10px}
.fcol ul{list-style:none;font-size:11px;color:#777}
.fcol li{line-height:24px}
.fcol li::before{content:"›";color:var(--blue-light);margin-right:7px;font-size:12px}
.bottom{left:0;top:1162px;width:1024px;height:38px;background:var(--bottom);color:#888;font-size:11px;padding:15px 136px}
.bottom b{color:#eee;font-weight:400}
</style>
</head>
<body>

<!-- top bar -->
<div class="abs topbar"></div>
<div class="abs lang">
  <div class="current"></div>
  <div class="flag" style="background:#2a3f8f"><span></span></div>
  <div class="flag"><span style="background:#2c9a45"></span><span style="background:#fff"></span><span style="background:#d8312d"></span></div>
  <div class="flag" style="flex-direction:column"><span style="background:#222"></span><span style="background:#d8312d"></span><span style="background:#f3c22a"></span></div>
  <div class="flag"><span style="background:#2a3f8f"></span><span style="background:#fff"></span><span style="background:#d8312d"></span></div>
</div>
<div class="abs account"><span>Login</span><span>Register</span></div>

<!-- header -->
<header class="abs header"></header>
<div class="abs brand" style="left:133px;top:44px"><span class="dot"></span><span class="name">Crestway Hub</span></div>
<nav class="abs nav" style="top:59px">
  <a class="active">Home</a><a>About</a><a>Talent</a><a>Companies</a><a>Jobs</a><a>Events</a><a>Contact</a>
</nav>
<div class="abs nav-underline"></div>

<!-- hero -->
<div class="abs hero-bg"></div>
<div class="abs map-fill" style="left:0" role="img" aria-label="Dotted world map decoration"></div>
<div class="abs map-fill" style="left:895px" role="img" aria-label="Dotted world map decoration"></div>
<div class="abs hero-photo" role="img" aria-label="Photo of a smiling businessman in a suit in a bright office with colleagues in the background"></div>
<div class="abs hero-person" role="img" aria-label="Businessman with arms crossed"></div>
<h1 class="abs hero-title">We always bring<br>excellence.</h1>
<p class="abs hero-sub">Linking People &amp; Firms<br>in Switzerland.</p>
<div class="abs arrow" style="left:81px"><svg width="14" height="14" viewBox="0 0 14 14"><path d="M9 2 4 7l5 5" fill="none" stroke="#fff" stroke-width="2"/></svg></div>
<div class="abs arrow" style="left:897px"><svg width="14" height="14" viewBox="0 0 14 14"><path d="m5 2 5 5-5 5" fill="none" stroke="#fff" stroke-width="2"/></svg></div>
<div class="abs dots"><i></i><i class="on"></i><i></i><i></i></div>

<!-- promo band -->
<section class="abs band"></section>
<div class="abs band-shade"></div>
<div class="abs card" style="left:136px">
  <div class="photo" style="left:0;width:190px;background:linear-gradient(180deg,#6b4f44 0%,#c99b84 35%,#e9e4df 65%,#2f3540 100%)" role="img" aria-label="Photo of a smiling young businesswoman"></div>
  <p style="right:32px;top:36px;text-align:right">Interested in the<br>Swiss Job Market?</p>
  <div class="btn" style="left:200px;top:134px">Register Now</div>
</div>
<div class="abs card" style="left:520px">
  <div class="photo" style="right:0;width:160px;background:linear-gradient(180deg,#7a5a48 0%,#c99f86 30%,#2c3850 55%,#1f2a3d 100%)" role="img" aria-label="Photo of a businessman working at a laptop"></div>
  <p style="left:32px;top:34px">Looking for talent for<br>specific job vacancies<br>in Switzerland?</p>
  <div class="btn" style="left:32px;top:134px">Post a Job</div>
</div>

<!-- latest jobs -->
<div class="abs section-title" style="left:138px;top:817px">
  <span class="rule" style="width:182px"></span>LATEST JOBS<span class="rule" style="width:182px"></span>
</div>
<div class="abs job-card">
  <div class="job-thumb">
    <div class="img" role="img" aria-label="Photo of a businessman in front of office towers"></div>
    <span class="tool" style="left:21px"><svg width="9" height="9" viewBox="0 0 9 9"><circle cx="3.7" cy="3.7" r="2.5" fill="none" stroke="#fff" stroke-width="1.2"/><path d="m5.6 5.6 2.6 2.6" stroke="#fff" stroke-width="1.3"/></svg></span>
    <span class="tool" style="left:42px"><svg width="9" height="9" viewBox="0 0 9 9"><path d="M3 6 6 3M2 5 1 6a1.4 1.4 0 0 0 2 2l1-1M7 4l1-1a1.4 1.4 0 0 0-2-2L5 2" fill="none" stroke="#fff" stroke-width="1"/></svg></span>
  </div>
  <div class="job-title">Front-End Developer at&nbsp; Brightforge</div>
  <div class="job-loc">Sydney, Australia</div>
  <div class="job-dots"><i class="on"></i><i></i><i></i><i></i><i></i><i></i><i></i><i></i><i></i><i></i></div>
  <p class="job-text">Lorem ipsum dolor sit amet, consectetur adipiscing elit. Proin nibh augue, suscipit a, scelerisque sed, lacinia in, mi. <a>Read More</a></p>
</div>

<!-- recent events -->
<div class="abs section-title" style="left:646px;top:819px">
  <span class="rule" style="width:52px"></span>RECENT EVENTS<span class="rule" style="width:52px"></span>
</div>
<div class="abs event" style="top:851px">
  <div class="thumb" role="img" aria-label="Photo of business people at an event"></div>
  <p>Fusce gravida tortor felis, ac dictum risus lorem ipsum dolor isment sagittis.<time>October 15, 2013</time></p>
</div>
<div class="abs event" style="top:913px">
  <div class="thumb" style="background:linear-gradient(160deg,#dfe7ee,#7f95a8)" role="img" aria-label="Photo of hands using a tablet"></div>
  <p>Fusce gravida tortor felis, ac dictum risus lorem ipsum dolor isment sagittis.<time>October 15, 2013</time></p>
</div>

<!-- footer -->
<footer class="abs footer"></footer>
<div class="abs brand" style="left:137px;top:1016px"><span class="dot" style="width:32px;height:32px"></span><span class="name" style="font-size:24px">Crestway Hub</span></div>
<p class="abs footer-about">Lorem ipsum dolor sit amet, consectetur adipiscing elit. Proin nibh augue, suscipit a, scelerisque sed, lacinia in, mi. Praesent sodales velit quis augue. Cras suscipit.</p>
<div class="abs fcol" style="left:391px;top:1018px">
  <h4>NAVIGATION</h4>
  <ul><li>Home</li><li>Jobs</li><li>Candidates</li><li>Partners</li></ul>
</div>
<div class="abs fcol" style="left:495px;top:1046px">
  <ul><li>About Us</li><li>Contact Us</li><li>Terms &amp; Conditions</li><li>Privacy Policy</li></ul>
</div>
<div class="abs fcol" style="left:647px;top:1018px">
  <h4>FOLLOW US</h4>
  <ul><li>Blog</li><li>Chirpline</li><li>Friendwall</li><li>Careerlink</li></ul>
</div>
<div class="abs fcol" style="left:775px;top:1018px">
  <h4>POPULAR JOBS</h4>
  <ul><li>Web Developer</li><li>Web Designer</li><li>UX Engineer</li><li>Account Manager</li></ul>
</div>
<div class="abs bottom">© Copyright 2014 <b>Company Website</b> | All Rights Reserved | Terms &amp; Conditions</div>

</body>
</html>
```